Teilnehmerzertifikat für Expeditionsmobil
Zielgruppe
Wir bitten alles Rund um das Thema Expeditionsmobil an. Unter anderem unsere Lagerfeuer und Weite Fahrt nach Tunesien und dafür benötige ich ein Teilnehmer Zertifikat.
Aufgabenstellung
Im Hintergrund soll ein Bild von der Sahara verarbeitet sein und im Vordergrund möchte ich von jedem Teilnehmer ein Bild mit dem eigenen Expeditonsfahrzeug einfügen. Das Zertifikat soll persöhnlich und wie von einem Freund sein

```html
<!DOCTYPE html>
<html lang="de">
<head>
<meta charset="utf-8">
<title>Teilnehmer-Zertifikat – Lagerfeuer und Weite Fahrt</title>
<link rel="stylesheet" href="https://fonts.googleapis.com/css2?family=Rubik+Dirt&family=Lexend:wght@300;400&family=Montserrat:wght@700;800&family=Great+Vibes&display=swap">
<style>
  :root {
    --ink: #0b0b0b;
    --red: #e3201f;
    --red-deep: #c8191a;
    --white: #ffffff;
    --sky: #8fb4d6;
    --sand: #b98d5c;
    --sand-dark: #8a6440;
    --paper: #f2f2f2;
  }
  * { box-sizing: border-box; margin: 0; padding: 0; }
  html, body { width: 1200px; height: 800px; overflow: hidden; background: var(--paper); }
  .certificate { position: relative; width: 1200px; height: 800px; overflow: hidden; background: var(--ink); }
  .backdrop { position: absolute; inset: 0; }
  .sahara-scene {
    position: absolute; left: 0; top: 0; width: 1200px; height: 420px;
    background: linear-gradient(180deg, var(--sky) 0%, #b7cde0 30%, #c9a272 48%, var(--sand) 70%, var(--sand-dark) 100%);
  }
  .bands { position: absolute; inset: 0; width: 1200px; height: 800px; }
  .title {
    position: absolute; left: 70px; top: 42px;
    font-family: "Rubik Dirt", sans-serif; font-size: 60px; line-height: 1.02;
    color: var(--white); letter-spacing: 2px; text-transform: uppercase;
  }
  .awarded {
    position: absolute; left: 300px; top: 185px;
    font-family: "Lexend", sans-serif; font-weight: 300; font-size: 30px; color: var(--white);
  }
  .name { position: absolute; left: 0; top: 262px; width: 640px; }
  .name-line {
    display: block; position: absolute;
    font-family: "Montserrat", sans-serif; font-weight: 800; font-size: 48px;
    color: var(--white); letter-spacing: 2px; line-height: 62px; padding: 0 18px;
  }
  .name-first { left: 250px; top: 0; width: 390px; background: var(--red); text-align: center; }
  .name-last { left: 270px; top: 62px; width: 370px; background: var(--ink); text-align: center; }
  .vehicle-photo {
    position: absolute; left: 665px; top: 150px; width: 360px; height: 290px;
    border: 12px solid var(--white);
    background: linear-gradient(180deg, #8a7d86 0%, #b27a4c 30%, #a8693f 60%, #8b5e44 100%);
    box-shadow: 0 6px 18px rgba(0,0,0,.35);
  }
  .message {
    position: absolute; left: 110px; top: 462px; width: 680px;
    font-family: "Lexend", sans-serif; font-weight: 400; font-size: 16px; line-height: 1.35;
    color: var(--white); text-align: center;
  }
  .message p + p { margin-top: 4px; }
  .signoff {
    position: absolute; left: 260px; top: 590px; display: flex; align-items: baseline; gap: 18px;
    color: var(--white);
  }
  .signoff-place { font-family: "Lexend", sans-serif; font-size: 16px; }
  .signoff-names { font-family: "Great Vibes", cursive; font-size: 46px; }
  .tour-mark {
    position: absolute; left: 810px; top: 480px; width: 300px;
    font-family: "Montserrat", sans-serif; font-weight: 800; font-size: 38px; line-height: 1.02;
    color: var(--white); text-transform: uppercase; text-align: center;
  }
  .brand {
    position: absolute; left: 740px; top: 712px; display: flex; align-items: center; gap: 14px;
  }
  .brand-dot { width: 40px; height: 40px; border-radius: 50%; background: var(--red); }
  .brand-name {
    font-family: "Montserrat", sans-serif; font-weight: 800; font-size: 34px;
    color: var(--red); text-transform: uppercase;
  }
</style>
</head>
<body>
<main class="certificate">
  <div class="backdrop">
    <div class="sahara-scene" role="img" aria-label="Foto der Sahara: blauer Himmel über Sanddünen mit Fahrzeugkolonne"></div>
    <svg class="bands" viewBox="0 0 1200 800" aria-hidden="true">
      <path fill="var(--ink)" d="M0 0H640 L655 30 L640 60 L668 95 L650 130 L672 170 L648 205 L660 240 L610 262 L560 250 L500 238 L420 230 L330 225 L250 222 L160 226 L80 232 L0 236Z"/>
      <path fill="var(--red)" d="M0 318 L60 308 L140 312 L230 304 L330 310 L440 302 L560 308 L660 300 L760 410 L860 412 L960 404 L1060 410 L1140 402 L1200 408 V800 H0Z"/>
      <path fill="var(--ink)" d="M0 608 L40 600 L70 612 L110 598 L150 610 L200 604 L260 616 L330 612 L400 626 L470 624 L540 636 L610 640 L680 652 L760 656 L820 662 L880 650 L920 660 L960 646 L1200 650 V800 H0Z"/>
    </svg>
  </div>

  <h1 class="title">Teilnehmer-<br>Zertifikat</h1>
  <p class="awarded">verliehen an:</p>

  <div class="name">
    <span class="name-line name-first">Maximillian</span>
    <span class="name-line name-last">Mustermann</span>
  </div>

  <div class="vehicle-photo" role="img" aria-label="Foto des Teilnehmers mit seinem roten Expeditionsmobil, das durch Wasser in der Wüste fährt"></div>

  <div class="message">
    <p>Ihr habt mit Begeisterung und Abenteuerlust an unserer gemeinsamen<br>Reise durch Tunesien teilgenommen.</p>
    <p>Mit eurem Expeditionsmobil habt ihr die Wüste bezwungen, neue<br>Freundschaften geschlossen und die Magie dieses einzigartigen Landes erlebt.</p>
    <p>Danke, dass ihr Teil dieser besonderen Tour wart – auf viele weitere Abenteuer!</p>
  </div>

  <div class="signoff">
    <span class="signoff-place">Tunisien, 21 November 2024</span>
    <span class="signoff-names">Jan &amp; Paul</span>
  </div>

  <div class="tour-mark">Lagerfeuer<br>und Weite<br>Fahrt</div>

  <div class="brand">
    <span class="brand-dot"></span>
    <span class="brand-name">Kranichpfad Reisen</span>
  </div>
</main>
</body>
</html>
```